Website Design for Luxury Product

Are you tired of the "same-old-same-old"?
Would you like to make a difference?
Do you want to make your mark as a designer and work on a full and cool project?
If you answered "YES" to any of the questions above ... keep on reading. We've been looking for you!
Our cigar company www.velmortabacs.com is in need of a new website design.
The look-and-feel needs to ooze luxury, be clean, and exciting.
Our goal is to have people visiting our website walk away and:
1. Understand that we are a high end, luxury cigar company
2. Feel a rapport and excitement with our company
3. Establish credibility
4. Have the visitor want to join our monthly VIP cigar club
Our logo is enclosed below
Frequently Asked Questions:
1. Who Is Your Target Market and What Are Your Demographics?
Our target market is 100% is the US and primarily males between the ages of 33 and 65.
Our target market are successful professionals like investment advisers, bankers, accountants, doctors, and entrepreneurs with a high disposable income.
Our audience has the ability to purchase just about anything they would like but prefer to purchase the highest quality items and don't mind paying a premium for this.
The website must give the visitor confidence that we are the "real thing" and that we are the best-of-the-best.
2. What Will The Website Be Hosted On?
The website will either be hosted as a stand alone website using Control Panel or on a WordPress Site.
3. What Font Should I Use For the Website?
Our standard font is the Gotham Family of Fonts.
4. What Colors Should the Website Use?
Surprise us.
Our goal is to have the website that is modern, hip, cool and oozes luxury.
5. What Look and Feel Should I Use?
Take a look at our newly designed logo which is attached as a file. We are after a look that is modern, clean, and luxurious.
If you think you have the "right stuff" we'd love to hear from you with your design.
Harold and Dwayne
Target Market(s)
Industry/Entity Type
Social Club
Coding
Coded - Design and coding required
Number of Pages Required
5+ page
Font styles to use
Other font styles liked:
- Gotham Family of Fonts
Requirements
Must have
- My project must have a home page and supporting pages with a consistent them that is
- Modern
- Luxurious
- Establishes Credibility
- For the content to use please look to our website with the existing wording.
Nice to have
- Use your imagination on this one.
Should not have
- Our project should not have a look and feel that is ornate and complicated. An example of this is our existing logo which can be found on our website www.velmortabacs.com
- We have moved away from this look.

```html
<!DOCTYPE html>
<html lang="en">
<head>
<meta charset="utf-8">
<title>Velmor Cigars</title>
<link href="https://fonts.googleapis.com/css2?family=Montserrat:ital,wght@0,300;0,400;0,500;0,600;0,700;1,400&display=swap" rel="stylesheet">
<style>
:root{
  --ink:#ffffff;
  --muted:#8a8c99;
  --dim:#5f6170;
  --yellow:#ffd800;
  --pink:#e8195a;
  --blue:#2aa8e0;
  --night:#1e1f2e;
  --deep:#0d0f17;
  --deeper:#0a0c13;
  --foot:#050608;
  --field:#0c0e15;
  --line:#2e3140;
}
*{margin:0;padding:0;box-sizing:border-box}
html,body{width:1200px;height:2647px;overflow:hidden;background:var(--deep)}
body{position:relative;font-family:'Montserrat',sans-serif;color:var(--ink)}
.abs{position:absolute}
section,header,footer{position:absolute;left:0;width:1200px}

/* hero */
.hero{top:0;height:529px;background:radial-gradient(ellipse at 70% 60%,#3a3f63 0%,#1d2036 45%,#121424 100%)}
.brand{left:256px;top:18px;width:92px;text-align:center}
.brand-mark{width:26px;height:26px;border:2px solid var(--ink);border-radius:50%;margin:0 auto 4px}
.brand-name{font-size:13px;font-weight:500;letter-spacing:2px;line-height:1.2}
.nav{top:30px;left:535px;display:flex;font-size:11px;font-weight:500}
.nav a{color:var(--ink);text-decoration:none;padding:7px 14px;line-height:14px}
.nav a.active{background:var(--yellow);color:#1a1a1a;padding:7px 25px}
.hero-title{top:186px;width:1200px;text-align:center;font-size:28px;font-weight:400;letter-spacing:.5px}
.hero-title strong{color:var(--yellow);font-weight:700}
.hero-rule{top:236px;left:538px;width:124px;height:2px;background:var(--pink)}
.hero-text{top:259px;width:1200px;text-align:center;font-size:14px;line-height:23px;font-weight:400}
.btn{display:block;text-align:center;text-decoration:none;color:var(--ink)}
.btn-pink{left:538px;top:341px;width:120px;height:28px;line-height:28px;border-radius:14px;background:var(--pink);font-size:9px;font-weight:700}

/* intro */
.intro{top:529px;height:396px;background:var(--night)}
.intro-item{width:210px}
.intro-item h3{font-size:21px;font-weight:300;margin-bottom:14px}
.intro-item p{font-size:9.5px;line-height:18px;color:var(--dim)}
.intro-item a{font-size:9.5px;color:var(--pink);text-decoration:none;display:block;line-height:16px;padding-left:4px}
.phone{left:496px;top:441px;width:208px;height:427px;border-radius:32px;background:#f2f2f4;border:2px solid #c9cacf;z-index:2}
.phone-speaker{left:84px;top:28px;width:40px;height:5px;border-radius:3px;background:#555}
.phone-screen{left:10px;top:52px;width:184px;height:326px;background:#fff}
.phone-bar{left:0;top:0;width:184px;height:14px;background:#1b1b1b}
.phone-art{left:8px;top:24px;width:168px;height:210px;background:linear-gradient(135deg,#d8b48a,#5a3622 55%,#8a5a36)}
.phone-home{left:88px;top:382px;width:32px;height:32px;border-radius:50%;border:2px solid #a5a6ab}

/* featured */
.featured{top:925px;height:443px;background:var(--deep)}
.featured-title{top:25px;width:1200px;text-align:center;font-size:21px;font-weight:700;color:var(--yellow)}
.featured-title span{border-bottom:2px solid var(--yellow);padding-bottom:1px}
.card{top:86px;width:222px;text-align:center}
.card-img{width:222px;height:152px}
.card h4{margin-top:20px;font-size:14px;font-weight:700;color:var(--pink)}
.card p{margin-top:6px;font-size:9.5px;line-height:18px;color:#d4d5dc;padding:0 10px}
.btn-white{margin:15px auto 0;width:108px;height:30px;line-height:30px;border-radius:15px;background:#fff;color:#333;font-size:9px}

/* quote */
.quote{top:1368px;height:298px;background:linear-gradient(100deg,#3a2a14 0%,#8a6a32 35%,#6e5228 60%,#b08244 80%,#4b3a22 100%)}
.quote-mark{width:1200px;text-align:center;font-size:64px;font-weight:700;color:var(--pink);line-height:1;font-family:Georgia,serif}
.quote-text{top:100px;width:1200px;text-align:center;font-size:17px;line-height:28px;font-style:italic}
.quote-by{top:179px;width:1200px;text-align:center;font-size:14px;font-style:italic}
.arrow{top:133px}

/* journey */
.journey{top:1666px;height:469px;background:radial-gradient(ellipse at 75% 40%,#3a4470 0%,#1b2038 50%,#0f1222 100%)}
.journey-title{top:30px;width:1200px;text-align:center;font-size:34px;font-weight:300;line-height:44px}
.journey-sub{left:252px;top:228px;font-size:20px;font-weight:700;color:var(--pink)}
.journey-text{left:252px;top:276px;width:305px;font-size:8.5px;line-height:14px;color:var(--muted)}
.btn-blue{left:252px;top:372px;width:90px;height:27px;line-height:27px;border-radius:14px;background:var(--blue);font-size:9px;font-weight:600}
.laptop-lid{left:584px;top:184px;width:408px;height:260px;border-radius:12px 12px 0 0;background:#111;border:2px solid #9c9ea6}
.laptop-screen{left:14px;top:14px;width:376px;height:230px;background:linear-gradient(135deg,#6b4a30,#c8936a 45%,#3a3a3a 75%,#9c7456)}
.laptop-base{left:540px;top:444px;width:496px;height:10px;border-radius:0 0 8px 8px;background:linear-gradient(#d8d9dd,#8f9096)}

/* contact */
.contact{top:2135px;height:433px;background:var(--deeper)}
.contact-title{left:205px;top:76px;font-size:41px;font-weight:700}
.contact-addr{left:205px;top:152px;font-size:11px;color:var(--dim)}
.contact-line{left:205px;font-size:18px;font-weight:600;color:#9fa1ad}
.contact-line span{color:var(--blue)}
.socials{left:205px;top:271px;display:flex;gap:22px}
.social{width:33px;height:33px;border-radius:50%;display:flex;align-items:center;justify-content:center}
.field{left:604px;width:383px;border:1px solid var(--line);background:var(--field);font-size:9px;color:#c9cad2;padding:10px 10px}
.btn-send{left:750px;top:327px;width:90px;height:25px;line-height:25px;border-radius:13px;background:var(--blue);font-size:9px;font-weight:600}

/* footer */
.footer{top:2568px;height:79px;background:var(--foot)}
.footer-nav{left:249px;top:35px;display:flex;gap:18px;font-size:8.5px;font-weight:500}
.footer-copy{right:95px;top:36px;font-size:8.5px;color:#c9cad2}
</style>
</head>
<body>

<header class="hero" role="img" aria-label="Blurred close-up of a cigar with glowing ember in deep blue light">
  <div class="abs brand">
    <div class="brand-mark"></div>
    <div class="brand-name">VELMOR</div>
  </div>
  <nav class="abs nav">
    <a class="active" href="#">HOME</a>
    <a href="#">VIP CLUB</a>
    <a href="#">OUR STORY</a>
    <a href="#">VELMOR BLEND</a>
    <a href="#">CONTACT</a>
  </nav>
  <h1 class="abs hero-title"><strong>LOREM IPSUM</strong> IS SIMPLY DUMMY</h1>
  <div class="abs hero-rule"></div>
  <p class="abs hero-text">Lorem Ipsum is simply dummy text of the printing and typesetting industry. Lorem Ipsum<br>has been the industry's standard dummy text ever since the 1500s</p>
  <a class="abs btn btn-pink" href="#">SHOW MORE</a>
</header>

<div class="abs phone">
  <div class="abs phone-speaker"></div>
  <div class="abs phone-screen">
    <div class="abs phone-bar"></div>
    <div class="abs phone-art" role="img" aria-label="Illustration of cigar leaves labelled filler and binder"></div>
  </div>
  <div class="abs phone-home"></div>
</div>

<section class="intro">
  <div class="abs intro-item" style="left:266px;top:80px">
    <h3>Who We Are</h3>
    <p>Lorem Ipsum is simply dummy text of the printing and typesetting industry. Lorem Ipsum has been the industry's standard</p>
    <a href="#">Read More...</a>
  </div>
  <div class="abs intro-item" style="left:266px;top:232px">
    <h3>Taste Profile</h3>
    <p>Fusce eu tortor tristique, varius sem sollicitudin, viverra ante. Curabitur id metus velit. Suspendisse in justo nulla</p>
    <a href="#">Read More...</a>
  </div>
  <div class="abs intro-item" style="left:748px;top:80px">
    <h3>Velmor VIP Club</h3>
    <p>Lorem Ipsum is simply dummy text of the printing and typesetting industry. Lorem Ipsum has been the industry's standard</p>
    <a href="#">Read More...</a>
  </div>
  <div class="abs intro-item" style="left:748px;top:232px">
    <h3>Velmor Story</h3>
    <p>Lorem Ipsum is simply dummy text of the printing and typesetting industry. Lorem Ipsum has been the industry's standard</p>
    <a href="#">Read More...</a>
  </div>
</section>

<section class="featured">
  <h2 class="abs featured-title"><span>FEATURED</span></h2>
  <article class="abs card" style="left:249px">
    <div class="card-img" role="img" aria-label="Hands rolling a cigar on a wooden table" style="background:linear-gradient(135deg,#7a3a1c,#c46a34 50%,#5a2a14)"></div>
    <h4>Lorem ipsum</h4>
    <p>Est a elit scelerisque vestibulum. Donec est sem, lobortis sit amet imperdiet vel, pretium lobortis erat. Nulla vitae</p>
    <a class="btn btn-white" href="#">Read more</a>
  </article>
  <article class="abs card" style="left:489px">
    <div class="card-img" role="img" aria-label="Close-up of shredded tobacco leaf" style="background:linear-gradient(135deg,#4a2a16,#9a6a44 50%,#3a2010)"></div>
    <h4>Lorem ipsum</h4>
    <p>Est a elit scelerisque vestibulum. Donec est sem, lobortis sit amet imperdiet vel, pretium lobortis erat. Nulla vitae</p>
    <a class="btn btn-white" href="#">Read more</a>
  </article>
  <article class="abs card" style="left:727px">
    <div class="card-img" role="img" aria-label="Single cigar presented in an open black gift box" style="background:linear-gradient(135deg,#f4f4f4,#bdbdbd 55%,#2a2a2a)"></div>
    <h4>Lorem ipsum</h4>
    <p>Est a elit scelerisque vestibulum. Donec est sem, lobortis sit amet imperdiet vel, pretium lobortis erat. Nulla vitae</p>
    <a class="btn btn-white" href="#">Read more</a>
  </article>
</section>

<section class="quote" role="img" aria-label="Warm toned photo of a hand holding a lit cigar">
  <div class="abs quote-mark" style="top:30px">&ldquo;</div>
  <p class="abs quote-text">We make a living by what we get, but we<br>make a life by what we give.</p>
  <p class="abs quote-by">-- Edmund Carrow</p>
  <div class="abs quote-mark" style="top:210px">&rdquo;</div>
  <svg class="abs arrow" style="left:224px" width="12" height="22" viewBox="0 0 12 22"><path d="M10 2 L2 11 L10 20" fill="none" stroke="#ffffff" stroke-width="1.5"/></svg>
  <svg class="abs arrow" style="left:960px" width="12" height="22" viewBox="0 0 12 22"><path d="M2 2 L10 11 L2 20" fill="none" stroke="#ffffff" stroke-width="1.5"/></svg>
</section>

<section class="journey">
  <h2 class="abs journey-title">You Are About To Embark On<br>A Journey Unlike Any You Have<br>Ever Experienced?</h2>
  <h3 class="abs journey-sub">Lorem ipsum dolor sit amet</h3>
  <p class="abs journey-text">Lorem ipsum dolor sit amet, consectetur adipiscing elit. Quisque molestie purus a felis condimentum molestie. Etiam a ullamcorper odio. Phasellus ipsum lorem, finibus semper sollicitudin ac, varius ut velit. Maecenas hendrerit ac ligula eu ultrices.</p>
  <a class="abs btn btn-blue" href="#">Show more</a>
  <div class="abs laptop-lid">
    <div class="abs laptop-screen" role="img" aria-label="Hands cutting cigars with a rolling press"></div>
  </div>
  <div class="abs laptop-base"></div>
</section>

<section class="contact">
  <h2 class="abs contact-title">Contact with us</h2>
  <p class="abs contact-addr">Linden Street 8/12 / Harlow County, Usa</p>
  <p class="abs contact-line" style="top:177px">Phone: <span>(+48) 512 700 318</span></p>
  <p class="abs contact-line" style="top:206px">E-mail: <span>contact@velmortabacs.com</span></p>
  <div class="abs socials">
    <span class="social" style="background:#2aa8e0"></span>
    <span class="social" style="background:#3b5998"></span>
    <span class="social" style="background:#c8232c"></span>
    <span class="social" style="background:#dd4b39"></span>
    <span class="social" style="background:#e8195a">
      <svg width="14" height="10" viewBox="0 0 14 10"><rect x="0.5" y="0.5" width="13" height="9" fill="none" stroke="#fff"/><path d="M0.5 0.5 L7 6 L13.5 0.5" fill="none" stroke="#fff"/></svg>
    </span>
  </div>
  <div class="abs field" style="top:78px;height:37px">Your Name</div>
  <div class="abs field" style="top:131px;height:35px">Your e-mail adress</div>
  <div class="abs field" style="top:180px;height:124px">Your message</div>
  <a class="abs btn btn-send" href="#">Send message</a>
</section>

<footer class="footer">
  <nav class="abs footer-nav">
    <span>HOME</span><span>VIP CLUB</span><span>OUR STORY</span><span>VELMOR BLEND</span><span>CONTACT</span>
  </nav>
  <p class="abs footer-copy">Copyright &copy; 2015. All rights reserved by velmor tabacs</p>
</footer>

</body>
</html>
```